Bright K's Auto Detailing new business cards

I am a business owner who professionally details cars. I clean and detail the interiors, exteriors of vehicles. I need a logo designed for my new business Bright K's Auto Detailing and a great designed card that will wow anyone that I hand it out to. Attached is a photo that I would like on side of the card. I want the picture to be on the right side of the card, while my busines name will be on the other side. I want the picture to have a slant where it divided the card into left and right, not just straight down. The picture will be printed glossy and I want the left half to have a carbon fiber background. Feel free to design a cool font for the business name, The business name needs to be a red gloss to pop out against the matte background. The back of the card should have my name Colin Marchetti. Under my name should be Owner/ Operator. then all my contact info and fb and instagram stuff. must include services offered- Paint Correction, Exterior detailing
Interior Detailing, Engine Bay Detailing, Headlight restoration, Ceramic Coatings

Target Market(s)

My target market is anyone who drives a vehicle.

Industry/Entity Type

Automotive

Contact Information for Business Card

Business name- Bright K's Auto Detailing
Colin Marchetti Owner/ Operator
Location- Cedar Hollow, CA
Business # (559) 214-6079
email- colin@thebrightpolisher.example
fb and instragram logos- @thebrightpolisher

Font styles to use
Serif
Script
Other font styles liked:
• Blacksword

Colors
ec1f27
000000

Requirements
Must have
• The card must be in landscape position. All the details that are in the brief description which are my business name, my name, services offered and any other info thats in the project description. I uploaded pics of veltranos that I would like to see different designs incorporated into the backside of the card. File 5,6,and 7 are ideas that I would like to see done with my business name. The diamond around my name with the polisher coming around the bottom, and a Veltrano outline on the left side of the diamond kinda like file 5
• Also, business name and name should be in some style of script, while the rest of the fonts in serif. Must have the picture of me on the front right side of the card!!!
Nice to have
• Your own personal ideas that you think I am missing.
Should not have
• No grafitti, no generic logos around the business name like every other auto detail card on google.

```html
<!DOCTYPE html>
<html lang="en">
<head>
<meta charset="utf-8">
<title>Bright K's Auto Detailing – Business Cards</title>
<link href="https://fonts.googleapis.com/css2?family=Great+Vibes&family=Tinos:wght@400;700&display=swap" rel="stylesheet">
<style>
  :root {
    --brand-red: #ec1f27;
    --ink-black: #000000;
    --carbon-dark: #0b0b0c;
    --carbon-mid: #1c1d1f;
    --paper-white: #ffffff;
    --soft-grey: #cfcfcf;
    --backdrop: #e4e1dc;
  }
  * { margin: 0; padding: 0; box-sizing: border-box; }
  html, body { width: 900px; height: 1200px; overflow: hidden; }
  body {
    background: var(--backdrop);
    font-family: "Tinos", "Times New Roman", serif;
    position: relative;
  }
  .card {
    position: absolute;
    left: 60px;
    width: 780px;
    height: 446px;
    border-radius: 16px;
    overflow: hidden;
    background: linear-gradient(135deg, var(--carbon-mid) 0%, var(--carbon-dark) 55%, #141416 100%);
    box-shadow: 0 10px 28px rgba(0,0,0,0.35);
  }
  .card--contact { top: 120px; }
  .card--front { top: 630px; }

  /* contact side */
  .car-photo {
    position: absolute; left: 0; top: 0; width: 470px; height: 446px;
    background: radial-gradient(ellipse at 40% 45%, #3a3b3f 0%, #1a1b1d 45%, rgba(11,11,12,0) 80%);
  }
  .owner-name {
    position: absolute; left: 34px; top: 28px;
    font-family: "Great Vibes", cursive;
    font-size: 42px; color: var(--paper-white); font-weight: 400;
    white-space: nowrap;
  }
  .owner-role {
    position: absolute; left: 36px; top: 84px;
    font-size: 14px; color: var(--brand-red);
  }
  .contact-list { position: absolute; left: 34px; top: 120px; list-style: none; }
  .contact-list li {
    display: flex; align-items: center; gap: 12px;
    color: var(--paper-white); font-size: 15px; height: 32px;
    white-space: nowrap;
  }
  .contact-icon {
    width: 20px; height: 20px; border-radius: 4px;
    background: var(--paper-white);
    display: flex; align-items: center; justify-content: center;
    flex-shrink: 0;
  }
  .social-row {
    position: absolute; left: 34px; top: 356px;
    display: flex; align-items: center; gap: 8px;
  }
  .social-square { width: 26px; height: 26px; background: #5a5b5e; border-radius: 4px; }
  .social-handle {
    background: var(--brand-red); color: var(--paper-white);
    font-size: 17px; padding: 4px 12px; border-radius: 3px;
    white-space: nowrap;
  }
  .brand-mark {
    position: absolute; color: var(--brand-red);
    font-family: "Tinos", "Times New Roman", serif; font-weight: 700;
    text-align: center; line-height: 1;
    white-space: nowrap;
  }
  .brand-mark .brand-top { display: block; font-size: 52px; }
  .brand-mark .brand-sub { display: block; font-size: 19px; letter-spacing: 3px; margin-top: 6px; }
  .card--contact .brand-mark { left: 440px; top: 56px; width: 320px; }
  .services {
    position: absolute; right: 36px; top: 228px; list-style: none; text-align: right;
  }
  .services li {
    color: var(--paper-white); font-size: 13px; letter-spacing: 0.5px;
    text-transform: uppercase; height: 19px; white-space: nowrap;
  }
  .red-bar {
    position: absolute; right: 0; top: 218px; width: 12px; height: 128px;
    background: var(--brand-red);
  }

  /* front side */
  .card--front .brand-mark { left: 60px; top: 170px; width: 330px; }
  .portrait-frame { position: absolute; left: 0; top: 0; width: 780px; height: 446px; }
</style>
</head>
<body>

<section class="card card--contact">
  <div class="car-photo" role="img" aria-label="Dark photo of a black sports car, faded into the carbon background"></div>
  <h1 class="owner-name">Colin Marchetti</h1>
  <p class="owner-role">Owner/ Operator</p>
  <ul class="contact-list">
    <li>
      <span class="contact-icon">
        <svg width="14" height="14" viewBox="0 0 24 24"><path d="M6.6 10.8a15 15 0 0 0 6.6 6.6l2.2-2.2c.3-.3.7-.4 1-.2 1.1.4 2.3.6 3.6.6.6 0 1 .4 1 1V20c0 .6-.4 1-1 1A17 17 0 0 1 3 4c0-.6.4-1 1-1h3.5c.6 0 1 .4 1 1 0 1.3.2 2.5.6 3.6.1.3 0 .7-.2 1z" fill="#000"/></svg>
      </span>
      Business # (559) 214-6079
    </li>
    <li>
      <span class="contact-icon">
        <svg width="14" height="14" viewBox="0 0 24 24"><rect x="2" y="5" width="20" height="14" rx="2" fill="#000"/><path d="M3 6l9 7 9-7" stroke="#fff" stroke-width="2" fill="none"/></svg>
      </span>
      colin@thebrightpolisher.example
    </li>
    <li>
      <span class="contact-icon">
        <svg width="14" height="14" viewBox="0 0 24 24"><path d="M12 2a7 7 0 0 0-7 7c0 5 7 13 7 13s7-8 7-13a7 7 0 0 0-7-7z" fill="#000"/><circle cx="12" cy="9" r="2.5" fill="#fff"/></svg>
      </span>
      Cedar Hollow, CA
    </li>
  </ul>
  <div class="social-row">
    <span class="social-square"></span>
    <span class="social-handle">@thebrightpolisher</span>
  </div>
  <div class="brand-mark">
    <span class="brand-top">Bright K's</span>
    <span class="brand-sub">AUTO DETAILING</span>
  </div>
  <ul class="services">
    <li>Paint Correction</li>
    <li>Exterior Detailing</li>
    <li>Interior Detailing</li>
    <li>Engine Bay Detailing</li>
    <li>Headlight Restoration</li>
    <li>Ceramic Coatings</li>
  </ul>
  <div class="red-bar"></div>
</section>

<section class="card card--front">
  <div class="brand-mark">
    <span class="brand-top">Bright K's</span>
    <span class="brand-sub">AUTO DETAILING</span>
  </div>
  <svg class="portrait-frame" viewBox="0 0 780 446">
    <defs>
      <linearGradient id="portrait-tone" x1="0" y1="0" x2="1" y2="1">
        <stop offset="0" stop-color="#6f7f92"/>
        <stop offset="0.5" stop-color="#2c3440"/>
        <stop offset="1" stop-color="#15181d"/>
      </linearGradient>
    </defs>
    <polygon points="480,20 762,20 762,426 480,426 428,223" fill="#ffffff"/>
    <polygon role="img" aria-label="Photo of the owner polishing a car with a rotary polisher" points="484,24 758,24 758,422 484,422 433,223" fill="url(#portrait-tone)"/>
  </svg>
</section>

</body>
</html>
```